Coffee Package Design

We need a new package design for a coffee company. Need to be a mix between modern and classic design combined together. We are open to different ideas.
We changing our product name from Café Verlona to Café Rostelli. The picture upload
shows what the product looks like. We want something completely different. The name of the company should go on the back of the package.
Updates

Hello Everyone,

Please read description, we are going with a new name and design for the product.

Café Rostelli. Café Verlona is what we are replacing with Café Rostelli, we are looking for new

look and design, please submit new designs.

There is a change in the description. Please take out Premium coffee blend and replace with Italian Roast.                                    

Industry/Entity Type

Cafe

Requirements
Must have
• You can use up to 6 colors.
Please put these items on design: Café Rostelli (this is the product name), Regular Premium Blend Coffee, 100% Arabica,
Dumbrell & Sons (name of the company), Tyler, TX on the back of the package

The file uploaded is an example of one of our products and how the package film
is sized.

```html
<!DOCTYPE html>
<html lang="en">
<head>
<meta charset="utf-8">
<title>Café Rostelli – Italian Roast Package Film</title>
<link rel="stylesheet" href="https://fonts.googleapis.com/css2?family=Marcellus&family=Josefin+Sans:wght@700&family=Playfair+Display:wght@400;600&display=swap">
<style>
  :root {
    --page: #ffffff;
    --film-grey: #e4e4e4;
    --ink-black: #0b0b0b;
    --roast-brown: #4a2c1a;
    --cream: #e9e6d2;
    --olive: #8d9a3c;
  }
  html, body {
    margin: 0;
    width: 1200px;
    height: 924px;
    overflow: hidden;
    background: var(--page);
  }
  .package-art { display: block; width: 1200px; height: 924px; }
  .brand-name { font-family: "Marcellus", serif; fill: var(--cream); }
  .badge-title { font-family: "Marcellus", serif; fill: var(--cream); }
  .badge-sub { font-family: "Marcellus", serif; fill: var(--olive); letter-spacing: 4px; }
  .variety { font-family: "Josefin Sans", sans-serif; font-weight: 700; fill: var(--cream); }
  .bean-origin { font-family: "Playfair Display", serif; fill: var(--cream); font-variant-numeric: lining-nums; }
  .maker { font-family: "Playfair Display", serif; fill: #ffffff; }
  .maker-name { font-weight: 600; }
</style>
</head>
<body>
<svg class="package-art" viewBox="0 0 1200 924" xmlns="http://www.w3.org/2000/svg">
  <defs>
    <linearGradient id="panelBlack" x1="0" y1="0" x2="0" y2="1">
      <stop offset="0" stop-color="#0a0a0a"/>
      <stop offset="0.6" stop-color="#1c1c1c"/>
      <stop offset="1" stop-color="#0a0a0a"/>
    </linearGradient>
    <radialGradient id="backGlow" cx="0.5" cy="0.45" r="0.7">
      <stop offset="0" stop-color="#222"/>
      <stop offset="1" stop-color="#0b0b0b"/>
    </radialGradient>
    <radialGradient id="roastWave" cx="0.5" cy="0.4" r="0.7">
      <stop offset="0" stop-color="#56321c"/>
      <stop offset="1" stop-color="#2a170d"/>
    </radialGradient>
    <radialGradient id="sealStrip" cx="0.4" cy="0.5" r="0.6">
      <stop offset="0" stop-color="#4f2e1a"/>
      <stop offset="1" stop-color="#1e120a"/>
    </radialGradient>

    <symbol id="frontPanel" viewBox="0 0 433 540">
      <rect class="front-border" x="0" y="0" width="433" height="540" fill="var(--roast-brown)"/>
      <rect class="front-field" x="12" y="0" width="409" height="532" fill="url(#panelBlack)"/>
      <path class="front-wave" d="M12,308 C80,340 160,352 240,332 S370,272 421,266 L421,532 L12,532 Z" fill="url(#roastWave)"/>
      <text class="brand-name" x="300" y="124" font-size="54" text-anchor="middle">Café</text>
      <text class="brand-name" x="218" y="218" font-size="90" text-anchor="middle">Rostelli</text>
      <g class="roast-badge">
        <rect x="133" y="250" width="160" height="96" rx="16" fill="#17120e" stroke="var(--cream)" stroke-width="2"/>
        <text class="badge-title" x="213" y="312" font-size="34" text-anchor="middle">ITALIAN</text>
        <text class="badge-sub" x="215" y="337" font-size="13" text-anchor="middle">ROAST</text>
      </g>
      <text class="variety" x="213" y="408" font-size="18" text-anchor="middle">REGULAR</text>
      <text class="bean-origin" x="213" y="459" font-size="21" text-anchor="middle">100% Arabica</text>
    </symbol>
  </defs>

  <g class="film-dieline">
    <rect class="edge-strip" x="86" y="31" width="10" height="540" fill="var(--ink-black)"/>
    <rect class="seal-margin" x="96" y="31" width="23" height="540" fill="var(--film-grey)"/>
    <rect class="seal-strip" x="119" y="31" width="74" height="540" fill="url(#sealStrip)"/>
    <rect class="side-panel" x="193" y="31" width="212" height="540" fill="url(#backGlow)"/>
    <text class="brand-name" x="352" y="456" font-size="30" text-anchor="middle">Café</text>
    <text class="brand-name" x="302" y="506" font-size="48" text-anchor="middle">Rostelli</text>

    <use href="#frontPanel" x="405" y="31" width="433" height="540"/>

    <rect class="back-panel" x="838" y="31" width="214" height="540" fill="var(--ink-black)"/>
    <text class="maker maker-name" transform="translate(968 298) rotate(-90)" font-size="20" text-anchor="middle">Dumbrell &amp; Sons</text>
    <text class="maker maker-place" transform="translate(995 296) rotate(-90)" font-size="17" text-anchor="middle">Dalwick, Ohio</text>
    <rect class="seal-margin" x="1052" y="31" width="73" height="540" fill="var(--film-grey)"/>
  </g>

  <g class="pack-fronts">
    <use href="#frontPanel" x="405" y="591" width="234" height="292"/>
    <use href="#frontPanel" x="650" y="591" width="234" height="292"/>
  </g>
</svg>
</body>
</html>
```